Anzeigengestaltung für Fliesenlegermeister
Zielgruppe
Ich bin ein Fliesenlegermeister und möchte mich selbstständig machen, ich saniere Bäder, Böden mit Fliesen, Fliesenspiegel und ich möchte eine Anzeige in den regionalen Zeitungen machen. Ich spreche alle Altersklassen mit Bädern für Sanierungen, Bodenfliesen und Neubauten an. Reparatur und Silikonarbeiten sowie Trockenbauarbeiten am eigenen Heim .
Aufgabenstellung
Ich möchte gern meine Kontaktdaten und die Farben vom Logo wieder finden,
als Beispiel habe ich meine aktuelle Visitenkarte beigefügt Dort finden sich die Kontaktdaten. Meine Arbeiten sind insbesondere :
Fliesenverlegung
Badsanierung
barrierefreie Bäder
Reparaturarbeiten
Silikonarbeiten
Trockenbau
Ob nun genau alle 6 Punkte in der Anzeige angezeigt werden soll bin ich mir nicht sicher oder ob nur 4 Beschreibungen reichen, damit es nicht zu viel wird.

```html
<!DOCTYPE html>
<html lang="de">
<head>
<meta charset="utf-8">
<title>Jonas Vellmer – Fliesenlegermeister</title>
<link href="https://fonts.googleapis.com/css2?family=Lato:wght@400;700;900&display=swap" rel="stylesheet">
<style>
  :root {
    --blue: #1d4f91;
    --grey: #4a4a4c;
    --grey-icon: #505052;
    --white: #ffffff;
    --photo-light: #f3f4f6;
    --photo-mid: #dfe2e6;
  }
  * { margin: 0; padding: 0; box-sizing: border-box; }
  html, body { width: 719px; height: 1200px; overflow: hidden; background: var(--white); }
  body { font-family: "Lato", Arial, sans-serif; color: var(--blue); }
  .ad { position: relative; width: 719px; height: 1200px; overflow: hidden; background: var(--white); }

  .hero-photo {
    position: absolute; left: 0; top: 0; width: 719px; height: 562px;
    background: linear-gradient(180deg, var(--photo-light) 0%, #e9ebee 55%, var(--photo-mid) 100%);
  }
  .headline {
    position: absolute; left: 309px; top: 200px;
    font-size: 39px; font-weight: 700; line-height: 1.2; color: var(--blue);
  }
  .call-badge {
    position: absolute; left: 447px; top: 441px; width: 232px; height: 232px;
    border-radius: 50%; background: var(--blue);
    display: flex; align-items: center; justify-content: center;
  }
  .call-badge p {
    transform: rotate(-12deg); text-align: center; color: var(--white);
    font-size: 23px; line-height: 1.25; font-weight: 400; margin-top: -10px;
  }

  .services { position: absolute; left: 41px; top: 594px; }
  .services h2 { font-size: 32px; font-weight: 700; margin-bottom: 6px; }
  .services ul { list-style: none; }
  .services li {
    display: flex; align-items: center; height: 42px;
    font-size: 26px; color: var(--blue);
  }
  .services li::before {
    content: ""; width: 18px; height: 18px; background: var(--blue);
    transform: rotate(45deg); margin: 0 20px 0 3px; flex: none;
  }

  .contact { position: absolute; left: 41px; top: 916px; list-style: none; }
  .contact li { display: flex; align-items: center; height: 40px; font-size: 25px; color: var(--blue); }
  .contact .icon {
    width: 27px; height: 23px; background: var(--grey-icon); margin-right: 28px;
    display: flex; align-items: center; justify-content: center; flex: none;
  }
  .contact b { font-weight: 700; }

  .brand { position: absolute; left: 44px; top: 1098px; display: flex; align-items: center; }
  .brand-mark { width: 34px; height: 34px; background: var(--blue); margin-right: 18px; flex: none; }
  .brand-name { font-size: 29px; font-weight: 700; color: var(--blue); white-space: nowrap; }

  .corner { position: absolute; right: 0; bottom: 0; }
</style>
</head>
<body>
<main class="ad">
  <div class="hero-photo" role="img" aria-label="Foto eines hellen, modernen Badezimmers mit Glasdusche, Waschtisch und freistehender Badewanne"></div>

  <h1 class="headline">Beste Qualität<br>direkt vom Meister</h1>

  <div class="call-badge">
    <p>Jetzt unverbindl.<br>telef. informieren<br>05307/2098415</p>
  </div>

  <section class="services">
    <h2>Alles aus einer Hand</h2>
    <ul>
      <li>Fliesenverlegung</li>
      <li>Badsanierung</li>
      <li>barrierefreie Bäder</li>
      <li>Reparaturarbeiten</li>
      <li>Silikonarbeiten</li>
      <li>Trockenbau</li>
    </ul>
  </section>

  <ul class="contact">
    <li><span class="icon"><svg width="14" height="14" viewBox="0 0 24 24"><path fill="#fff" d="M6.6 10.8a15.1 15.1 0 0 0 6.6 6.6l2.2-2.2c.3-.3.7-.4 1-.2 1.1.4 2.3.6 3.6.6.6 0 1 .4 1 1V20c0 .6-.4 1-1 1A17 17 0 0 1 3 4c0-.6.4-1 1-1h3.5c.6 0 1 .4 1 1 0 1.3.2 2.5.6 3.6.1.3 0 .7-.2 1z"/></svg></span>05307/2098415&nbsp;<b>Mobil</b>&nbsp;01731495260</li>
    <li><span class="icon"><svg width="15" height="11" viewBox="0 0 15 11"><rect x="0.75" y="0.75" width="13.5" height="9.5" fill="none" stroke="#fff" stroke-width="1.5"/><path d="M1 1l6.5 5L14 1" fill="none" stroke="#fff" stroke-width="1.5"/></svg></span>info@fliesenlegermeister-vellmer.de</li>
    <li><span class="icon"><svg width="12" height="16" viewBox="0 0 12 16"><path fill="#fff" d="M6 0a6 6 0 0 0-6 6c0 4.5 6 10 6 10s6-5.5 6-10a6 6 0 0 0-6-6zm0 8.5A2.5 2.5 0 1 1 6 3.5a2.5 2.5 0 0 1 0 5z"/></svg></span>Lindenhofstraße 12 • 38110 Braunschweig</li>
  </ul>

  <div class="brand">
    <div class="brand-mark"></div>
    <div class="brand-name">Jonas Vellmer Fliesenlegermeister</div>
  </div>

  <svg class="corner" width="719" height="1200" viewBox="0 0 719 1200" aria-hidden="true">
    <polygon points="606,1012 719,899 719,980 646,1053" fill="var(--grey)"/>
    <polygon points="530,1200 719,1200 719,1011" fill="var(--blue)"/>
  </svg>
</main>
</body>
</html>
```